need professional, precise design for a website

I will start with a homepage design and if we pick your design, we'll have you design up to 6 more interior pages (we'll pay extra for these of course). We need a homepage design for a reserve study company based in Idaho, covering the northwest region. The company is called copper ridge capital study. Their current site is at https://www.copperridgecapital.example/ and they really like this site for inspiration https://www.fundplanhub.example/ but they would like an original design, just more modern and fresh like the sample site. I have logo files I will attach. They want something that looks financial and has a feel of accuity. Their main call to action will be to have someone fill in a contact form or call them on the phone. They will have a sample study that someone can download as on the fundplanhub site. You can use copy from their current site.

```html
<!DOCTYPE html>
<html lang="en">
<head>
<meta charset="UTF-8">
<title>Copper Ridge Capital Study — Home</title>
<link href="https://fonts.googleapis.com/css2?family=Arimo:wght@400;700&family=Open+Sans:wght@400;600&family=Roboto:wght@300;400&display=swap" rel="stylesheet">
<style>
:root{
  --green:#8db52c;
  --green-veil:rgba(141,181,44,.72);
  --ink:#2f2f2f;
  --muted:#555;
  --footer:#3b3b3b;
  --footer-dark:#2a2a2a;
  --sage:#e6ebd3;
  --step-gray:#6f7768;
  --step-blue:#2e86c1;
  --step-teal:#2f8c8f;
}
*{margin:0;padding:0;box-sizing:border-box}
html,body{width:1200px;height:1200px;overflow:hidden;background:#fff}
.canvas{width:1500px;height:1500px;transform:scale(.8);transform-origin:0 0;position:relative;font-family:"Arimo",Arial,sans-serif;color:var(--ink)}
.page{position:absolute;left:540px;top:36px;width:422px;height:1414px}
.abs{position:absolute}
.caps{text-transform:uppercase}

/* hero */
.hero{left:0;top:0;width:422px;height:227px;background:linear-gradient(180deg,#5f8aa6 0%,#88a9bd 35%,#7a8f8f 62%,#3f8a5e 85%,#2f7a52 100%)}
.nav{left:0;top:0;width:422px;height:32px;background:rgba(40,60,80,.55);display:flex;justify-content:flex-end;align-items:center;padding-right:18px;gap:0}
.nav a{color:#fff;font-size:6.2px;text-decoration:none;padding:0 4.5px;height:32px;line-height:32px}
.nav a.active{background:#8a8f94;font-weight:700}
.hero-copy{left:40px;top:84px;width:342px;text-align:center;color:#fff;font-size:6.8px;line-height:9px}
.cta{left:150px;top:117px;width:124px;height:18px;background:var(--green);color:#fff;font-size:7.5px;text-align:center;line-height:18px}

/* stats */
.intro{left:0;top:258px;width:422px;text-align:center;font-size:7.6px;line-height:10px;color:var(--ink)}
.stat{top:292px;text-align:center}
.stat .num{font-family:"Roboto",sans-serif;font-weight:300;font-size:46px;line-height:48px;color:#333}
.stat .num small{font-size:16px}
.stat .label{font-size:7.4px;line-height:10px;color:var(--muted)}
.divider{top:296px;width:1px;height:66px;background:#ddd}

/* services */
.services{left:0;top:409px;width:422px;height:284px;overflow:hidden;background:#a8a8a4}
.service{color:#fff;font-size:6.8px;line-height:9px}
.service b{font-size:7.6px}
.service .more{font-size:5.6px;font-weight:700}

/* statement */
.statement{left:0;top:724px;width:422px;text-align:center;font-size:7.6px;line-height:10px}

/* key results */
.results{left:0;top:774px;width:422px;height:242px;overflow:hidden;background:#7d9a5a}
.step{width:42px;height:42px;border-radius:50%;color:#fff;font-family:"Open Sans",sans-serif;font-size:21px;line-height:42px;text-align:center}
.step-text{color:#fff;font-family:"Open Sans",sans-serif;font-size:7.6px;line-height:11px}

/* team */
.who{left:0;top:1040px;width:422px;text-align:center}
.who h2{font-family:"Open Sans",sans-serif;font-weight:600;font-size:14px;line-height:18px}
.who p{font-size:7.6px;line-height:10px}
.team{left:0;top:1091px;width:422px;height:150px;background:var(--sage)}
.portrait{border-radius:50%;background:radial-gradient(circle at 50% 40%,#d9c3a6,#8f8a6e 70%,#6d7558)}

/* footer */
.contact-now{left:316px;top:1263px;font-size:7.6px;color:#888}
.footer{left:0;top:1280px;width:422px;height:134px;background:var(--footer);overflow:hidden}
.footer h3{font-size:10.5px;color:#fff}
.footer p{font-size:6.6px;line-height:9px;color:#fff}
.links a{display:block;color:#fff;font-size:6.6px;text-decoration:none;border-bottom:1px solid #777;width:58px;height:13px;line-height:12px}
.field{border:1px solid #888;font-size:5.6px;color:#888;padding:2px 6px}
.social{width:15px;height:15px;border-radius:50%;border:1px solid #fff}
</style>
</head>
<body>
<div class="canvas">
<div class="page">

  <section class="abs hero" role="img" aria-label="Photograph of a street of large suburban houses under a cloudy sky"></section>
  <nav class="abs nav caps">
    <a class="active" href="#">Home</a><a href="#">Reserve Study</a><a href="#">Projects</a><a href="#">Who We Are</a><a href="#">About Us</a><a href="#">Contact Us</a>
  </nav>
  <p class="abs hero-copy caps">Lorem ipsum dolor sit amet, consectetuer adipiscing elit. Aenean commodo ligula eget dolor. Aenean massa. Cum sociis natoque penatibus et magnis dis parturient montes, nascetur ridiculus mus.</p>
  <a class="abs cta caps">Request a proposal</a>

  <p class="abs intro caps">Each year, thousands of managers, board members, and<br>facility directors trust us to create their reserve funding plans</p>
  <div class="abs stat" style="left:28px;width:66px"><div class="num">30</div><div class="label caps">Years<br>experience</div></div>
  <div class="abs divider" style="left:104px"></div>
  <div class="abs stat" style="left:112px;width:152px"><div class="num">52000<small>+</small></div><div class="label caps">Reserve studies<br>completed</div></div>
  <div class="abs divider" style="left:272px"></div>
  <div class="abs stat" style="left:284px;width:104px"><div class="num"><small>$</small>300</div><div class="label caps">Million funding<br>guidance provided</div></div>

  <section class="abs services">
    <div class="abs" role="img" aria-label="Photograph of a tall historic stone building seen from below" style="left:0;top:0;width:422px;height:284px;background:linear-gradient(120deg,#cfcfcd 0%,#a3a29c 40%,#8d8c84 100%)"></div>
    <svg class="abs" width="422" height="284" style="left:0;top:0"><polygon points="40,0 422,0 422,284 60,284 170,160 150,30" fill="var(--green-veil)"/></svg>
    <svg class="abs" width="20" height="24" style="left:102px;top:8px"><rect x="2" y="2" width="16" height="20" fill="none" stroke="#3a4a2a" stroke-width="1.5"/><path d="M6 6h3M11 6h3M6 11h3M11 11h3M6 16h3M11 16h3" stroke="#3a4a2a"/></svg>
    <div class="abs service caps" style="left:130px;top:7px"><b>Association governed communities.</b><br>Condos, co-ops, HOAs, POAs, PUDs, townhomes, etal.<br><span class="more">Learn more</span></div>
    <div class="abs service caps" style="left:194px;top:49px"><b>School &amp; colleges</b><br>Private and public schools, school districts,<br>colleges and universities<br><span class="more">Learn more</span></div>
    <svg class="abs" width="28" height="28" style="left:160px;top:125px"><circle cx="14" cy="14" r="12" fill="none" stroke="#2f3a22" stroke-width="1.5"/><path d="M2 14h24M14 2v24M6 6q8 8 16 0M6 22q8-8 16 0" fill="none" stroke="#2f3a22"/></svg>
    <div class="abs service caps" style="left:192px;top:121px"><b>Clubs &amp; parties</b><br>Private and public schools, school districts,<br>colleges and universities<br><span class="more">Learn more</span></div>
    <div class="abs service caps" style="left:192px;top:192px"><b>Swiming pools</b><br>Private and public schools, school districts,<br>colleges and universities<br><span class="more">Learn more</span></div>
    <div class="abs service caps" style="left:134px;top:242px"><b>Sports and play grounds</b><br>Private and public schools, school districts,<br>colleges and universities<br><span class="more">Learn more</span></div>
  </section>

  <p class="abs statement caps"><b>Our reserve studies clearly spell out what needs to be<br>reserved for,evaluate the strength of the current reserve<br>fund and recommend a funding plan.</b><br>Every reserve study includes three key results</p>

  <section class="abs results">
    <div class="abs" role="img" aria-label="Photograph of a large house with lawn and a garden pool" style="left:0;top:0;width:422px;height:242px;background:linear-gradient(160deg,#8fb3d8 0%,#6d8a5a 30%,#7f9a4e 60%,#5f7d3a 100%)"></div>
    <svg class="abs" width="422" height="242" style="left:0;top:0"><polygon points="160,0 422,0 422,242 160,242" fill="rgba(141,181,44,.55)"/></svg>
    <div class="abs step" style="left:167px;top:28px;background:var(--step-gray)">1</div>
    <p class="abs step-text caps" style="left:215px;top:38px">Component list- detailing the scope and<br>schedule of all reserve projects</p>
    <div class="abs step" style="left:167px;top:93px;background:var(--step-blue)">2</div>
    <p class="abs step-text caps" style="left:215px;top:102px">Calculation of reserve fund strength<br>(% funded)</p>
    <div class="abs step" style="left:167px;top:166px;background:var(--step-teal)">3</div>
    <p class="abs step-text caps" style="left:215px;top:165px">Custom funding plan going forward<br>that allows for timely repairs &amp;<br>replacements with an emphasis on<br>avoiding supplemental funding sources</p>
  </section>

  <div class="abs who"><h2 class="caps">Who we are !</h2><p class="caps">Lorem ipsum is simply dummy text of the printing and typesetting<br>industry standard dummy text ever since the 1500s,</p></div>

  <section class="abs team">
    <div class="abs portrait" role="img" aria-label="Team member portrait" style="left:41px;top:28px;width:90px;height:90px"></div>
    <div class="abs portrait" role="img" aria-label="Team member portrait" style="left:151px;top:13px;width:122px;height:122px;border:2px solid #c9c2b4"></div>
    <div class="abs portrait" role="img" aria-label="Team member portrait" style="left:296px;top:32px;width:82px;height:82px;background:radial-gradient(circle at 50% 40%,#d6a882,#6e7f58 70%,#2f5d9a)"></div>
  </section>

  <svg class="abs" width="38" height="34" style="left:285px;top:1246px"><path d="M2 18L36 2L24 32L18 20Z M18 20L36 2" fill="none" stroke="#666" stroke-width="1.3"/><path d="M4 26l8-4M6 31l8-5" stroke="#666"/></svg>
  <span class="abs contact-now caps">Contact now</span>

  <footer class="abs footer">
    <svg class="abs" width="422" height="134" style="left:0;top:0"><polygon points="0,0 203,0 70,134 0,134" fill="var(--footer-dark)"/></svg>
    <div class="abs" style="left:23px;top:18px;width:110px"><h3 class="caps">About us</h3><p>Lorem ipsum dolor sit amet, consectetuer adipiscing elit. Aenean commodo ligula eget dolor. Aenean massa.</p></div>
    <p class="abs" style="left:25px;top:80px;font-size:10px;color:#fff">Follow@</p>
    <div class="abs" style="left:25px;top:97px;display:flex;gap:4px"><span class="social"></span><span class="social"></span><span class="social"></span><span class="social"></span></div>
    <div class="abs links caps" style="left:174px;top:19px"><a>Our projects</a><a>Our team</a><a>Who we are</a><a>About us</a><a>Contact us</a></div>
  </footer>
  <div class="abs" style="left:286px;top:1262px;width:110px;height:139px;border:1px solid #888;border-top:none"></div>
  <div class="abs field" style="left:287px;top:1284px;width:108px;height:13px">Full Name</div>
  <div class="abs field" style="left:287px;top:1301px;width:108px;height:13px">Email Address</div>
  <div class="abs field" style="left:287px;top:1319px;width:108px;height:60px">Leave us Message</div>
  <div class="abs field caps" style="left:295px;top:1385px;width:92px;height:14px;text-align:center">Send it now</div>

</div>
</div>
</body>
</html>
```